Drag Show Flyer

We are holding a Drag Show, we are looking for something fun and exciting, over the top is a must.

Show Date: Saturday September 2nd 2017
Venue: Pelican Row Cafe Bunbury
Doors open 7pm
Tickets: $50 per person, includes glass of sparkling on arrival and canapes
Tickets available at the Venue or from ticketloom.com.au

Target Market(s)

Female, Hens Party, LBGT

Industry/Entity Type

Entertainment

Colors

Designer to choose colors to be used in the design.

Requirements
Must have
• Show Date: Saturday September 2nd 2017
• Venue: Pelican Row Cafe Bunbury
• Doors open 7pm
• Tickets: $50 per person, includes glass of sparkling on arrival and canapes
• Tickets available at the Venue or from ticketloom.com.au

```html
<!DOCTYPE html>
<html lang="en">
<head>
<meta charset="UTF-8">
<title>Drag Show Flyer</title>
<link href="https://fonts.googleapis.com/css2?family=Bebas+Neue&family=Bungee&family=Lato:wght@400;700&family=Roboto+Condensed:wght@300;700&display=swap" rel="stylesheet">
<style>
  :root {
    --page: #efebe6;
    --ink: #050302;
    --gold: #f6c60f;
    --white: #ffffff;
    --amber: #e07a1c;
    --chrome: #f3dcc4;
    --rule: rgba(255,255,255,0.45);
  }
  * { margin: 0; padding: 0; box-sizing: border-box; }
  html, body {
    width: 1200px; height: 1200px; overflow: hidden;
    background: var(--page);
  }
  .flyer {
    position: absolute; left: 195px; top: 30px;
    width: 810px; height: 1140px;
    background: var(--ink);
    overflow: hidden;
    color: var(--white);
    text-align: center;
  }
  .hero-photo {
    position: absolute; left: 0; top: 0; width: 810px; height: 660px;
    background:
      radial-gradient(ellipse 120px 190px at 420px 250px, rgba(255,240,225,0.95), rgba(230,170,120,0.85) 45%, rgba(170,90,40,0.55) 75%, transparent 100%),
      radial-gradient(ellipse 230px 300px at 415px 280px, rgba(220,140,70,0.6), transparent 100%),
      radial-gradient(ellipse 60px 110px at 420px 500px, rgba(200,140,90,0.6), transparent 100%),
      radial-gradient(circle 55px at 150px 28px, rgba(255,235,150,1), rgba(255,180,60,0.6) 55%, transparent),
      radial-gradient(circle 45px at 32px 98px, rgba(255,225,140,0.95), rgba(255,160,50,0.5) 55%, transparent),
      radial-gradient(ellipse 200px 260px at 140px 300px, rgba(255,140,30,0.95), rgba(210,95,20,0.6) 55%, transparent 100%),
      radial-gradient(ellipse 160px 160px at 300px 520px, rgba(255,120,20,0.8), transparent 100%),
      linear-gradient(180deg, #4a1c06 0%, #2a1005 55%, var(--ink) 100%);
  }
  .crowd-photo {
    position: absolute; left: 0; bottom: 0; width: 810px; height: 270px;
    background:
      radial-gradient(ellipse 460px 150px at 405px 70px, rgba(200,130,40,0.6), transparent 80%),
      radial-gradient(circle 6px at 760px 60px, rgba(255,220,150,0.9), transparent),
      linear-gradient(180deg, transparent 0%, #2a1a08 40%, #0a0604 100%);
  }
  .title {
    position: absolute; left: 0; right: 0; top: 510px;
    font-family: "Bungee", "Bebas Neue", sans-serif; font-weight: 400;
    font-size: 84px; line-height: 1; letter-spacing: 4px;
    color: var(--gold);
    background: radial-gradient(circle, var(--gold) 1.6px, transparent 2.2px) 0 0 / 5px 5px;
    -webkit-background-clip: text; background-clip: text;
    -webkit-text-fill-color: transparent;
    filter: drop-shadow(0 0 6px rgba(246,198,15,0.35));
  }
  .date {
    position: absolute; left: 0; right: 0; top: 612px;
    font-family: "Bebas Neue", sans-serif;
    font-size: 62px; line-height: 1;
    transform: scaleX(0.86);
  }
  .venue {
    position: absolute; left: 0; right: 0; top: 676px;
    font-family: "Roboto Condensed", sans-serif; font-weight: 300;
    font-size: 38px; line-height: 1;
  }
  .divider {
    position: absolute; left: 135px; width: 540px; top: 730px; height: 1px;
    background: linear-gradient(90deg, transparent, var(--rule), transparent);
  }
  .doors {
    position: absolute; left: 0; right: 0; top: 746px;
    font-family: "Roboto Condensed", sans-serif; font-weight: 700;
    font-size: 37px; line-height: 1; color: var(--gold);
  }
  .price {
    position: absolute; left: 0; right: 0; top: 786px;
    font-family: "Bebas Neue", sans-serif;
    font-size: 92px; line-height: 1;
    transform: scaleX(0.92);
  }
  .price .amount { color: var(--gold); }
  .includes {
    position: absolute; left: 0; right: 0; top: 878px;
    font-family: "Lato", sans-serif; font-size: 14px; letter-spacing: 0.1px;
  }
  .partners {
    position: absolute; left: 0; right: 0; top: 922px;
    display: flex; justify-content: center; gap: 14px;
  }
  .partner {
    background: var(--white); color: var(--ink);
    font-family: "Lato", sans-serif; font-weight: 700; font-size: 10px;
    height: 44px; padding: 0 8px;
    display: flex; align-items: center; gap: 6px;
  }
  .partner .dot { width: 20px; height: 20px; border-radius: 50%; background: var(--ink); flex: none; }
  .partner.dark { background: var(--ink); color: var(--white); border: 2px solid var(--white); }
  .tickets {
    position: absolute; left: 0; right: 0; top: 1082px;
    font-family: "Lato", sans-serif; font-size: 19px; font-weight: 700;
  }
</style>
</head>
<body>
  <main class="flyer">
    <div class="hero-photo" role="img" aria-label="Glowing vintage chrome stage microphone in front of a brass trumpet under bright orange spotlights"></div>
    <div class="crowd-photo" role="img" aria-label="Silhouetted crowd with raised hands under golden stage light"></div>

    <h1 class="title">DRAG SHOW</h1>
    <p class="date">Saturday September 2nd 2017</p>
    <p class="venue">PELICAN ROW CAFE BUNBURY</p>
    <div class="divider"></div>
    <p class="doors">DOORS OPEN 7PM</p>
    <p class="price"><span class="amount">$50</span> PER PERSON</p>
    <p class="includes">INCLUDES GLASS OF SPARKLING ON ARRIVAL &amp; CANAPES</p>

    <div class="partners">
      <div class="partner">Rouge Nights</div>
      <div class="partner dark">Pelican Row Cafe</div>
      <div class="partner"><span class="dot"></span>Harbour Lane Group</div>
    </div>

    <p class="tickets">Tickets Available at The Venue or from ticketloom.com.au</p>
  </main>
</body>
</html>
```